Harbourline Refrigeration business card design

We would like a new design for our business card as we have a new logo.
We need generic business card to give our customers with our office details - with the option of making it individualized for each manager

Target Market(s)

Companies and homeowners

Industry/Entity Type

Air Conditioning

Contact Information for Business Card

We are not sure if we want single or double sided it will depend on the design we choose

Colors
33a6d7
0255a3

Requirements
Must have
• Logo
• phone: (08) 8721 5940
• email: harbourserve@tealnet.example
• website: www.harbourlinerefrigeration.example
• AU61420
• BLD472913
Nice to have
• Address - Shed 5/284 Tallis Rd, Port Calloway SA 5712

```html
<!DOCTYPE html>
<html lang="en">
<head>
<meta charset="utf-8">
<title>Harbourline Refrigeration – Business Card</title>
<link href="https://fonts.googleapis.com/css2?family=Open+Sans:wght@400;600;700&display=swap" rel="stylesheet">
<style>
  :root {
    --bg: #e6e3e0;
    --paper: #ffffff;
    --brand-dark: #0255a3;
    --brand-light: #33a6d7;
    --ink: #3b3f45;
    --divider: #a8505a;
    --emboss: #0a4a8a;
    --web-text: #8fd0f2;
    --web-rule: #5fb7e6;
  }
  html, body {
    margin: 0;
    width: 1200px;
    height: 997px;
    overflow: hidden;
    background: var(--bg);
    font-family: "Open Sans", Arial, sans-serif;
  }
  .card {
    position: absolute;
    left: 250px;
    width: 700px;
    height: 400px;
    overflow: hidden;
    box-shadow: 0 6px 18px rgba(0,0,0,0.12);
  }
  /* Front side */
  .card--front { top: 62px; background: var(--paper); }
  .brand {
    position: absolute;
    left: 40px;
    top: 150px;
    width: 245px;
    display: flex;
    align-items: center;
    gap: 12px;
  }
  .brand__dot {
    flex: none;
    width: 30px;
    height: 30px;
    border-radius: 50%;
    background: var(--brand-light);
  }
  .brand__name {
    margin: 0;
    font-weight: 700;
    font-size: 27px;
    line-height: 1.1;
    color: var(--brand-dark);
  }
  .card__divider {
    position: absolute;
    left: 300px;
    top: 40px;
    width: 1px;
    height: 215px;
    background: var(--divider);
    opacity: 0.7;
  }
  .contact {
    position: absolute;
    left: 325px;
    top: 42px;
    color: var(--ink);
    font-size: 15px;
    line-height: 1.5;
  }
  .contact__name {
    margin: 0;
    font-weight: 700;
    font-size: 21px;
    color: var(--brand-dark);
  }
  .contact__role { margin: 0 0 6px; font-size: 14px; }
  .contact__line { display: flex; align-items: center; gap: 8px; margin: 0; }
  .contact__line svg { width: 13px; height: 13px; fill: var(--brand-dark); flex: none; }
  .contact__address { margin: 8px 0 0; }
  .band { position: absolute; left: 0; bottom: 0; width: 700px; height: 140px; }
  .licences {
    position: absolute;
    right: 14px;
    bottom: 98px;
    background: var(--paper);
    color: var(--brand-dark);
    font-size: 15px;
    font-weight: 600;
    padding: 2px 12px;
    letter-spacing: 0.5px;
  }
  /* Back side */
  .card--back {
    top: 527px;
    background: linear-gradient(160deg, #1a9ad8 0%, #0c73bb 50%, #034f96 100%);
  }
  .back__name {
    position: absolute;
    left: 0; right: 0;
    top: 120px;
    margin: 0;
    text-align: center;
    font-weight: 700;
    font-size: 46px;
    line-height: 1.1;
    color: var(--emboss);
    text-shadow: 0 1px 0 rgba(255,255,255,0.12);
  }
  .back__web {
    position: absolute;
    left: 0; right: 0;
    bottom: 70px;
    display: flex;
    align-items: center;
    justify-content: center;
    gap: 14px;
    color: var(--web-text);
    font-size: 15px;
    letter-spacing: 1px;
  }
  .back__rule { width: 90px; height: 1px; background: var(--web-rule); opacity: 0.7; }
</style>
</head>
<body>

<section class="card card--front" aria-label="Business card front">
  <div class="brand">
    <span class="brand__dot"></span>
    <p class="brand__name">Harbourline Refrigeration</p>
  </div>

  <div class="card__divider"></div>

  <div class="contact">
    <p class="contact__name">Daniel Reeve</p>
    <p class="contact__role">Director</p>
    <p class="contact__line">
      <svg viewBox="0 0 16 16" aria-hidden="true"><path d="M3.6 1.5l2.3 2.6-1.3 1.9c.9 2 2.4 3.6 4.4 4.5l1.9-1.3 2.6 2.3-1.1 2.2C7.6 13.5 2.5 8.4 1.4 2.6z"/></svg>
      (08) 8721 5940
    </p>
    <p class="contact__line">
      <svg viewBox="0 0 16 16" aria-hidden="true"><path d="M1 3h14v10H1z M2 4l6 5 6-5" fill="none" stroke="#0255a3" stroke-width="1.6"/></svg>
      harbourserve@tealnet.example
    </p>
    <p class="contact__line">
      <svg viewBox="0 0 16 16" aria-hidden="true"><circle cx="8" cy="8" r="6.5" fill="none" stroke="#0255a3" stroke-width="1.5"/><path d="M1.5 8h13M8 1.5c-3 3.5-3 9.5 0 13M8 1.5c3 3.5 3 9.5 0 13" fill="none" stroke="#0255a3" stroke-width="1.1"/></svg>
      www.harbourlinerefrigeration.example
    </p>
    <p class="contact__address">Shed 5/284 Tallis Rd,<br>Port Calloway SA 5712</p>
  </div>

  <svg class="band" viewBox="0 0 700 140" preserveAspectRatio="none" aria-hidden="true">
    <defs>
      <linearGradient id="bandFill" x1="0" y1="0" x2="1" y2="0">
        <stop offset="0" stop-color="#0255a3"/>
        <stop offset="1" stop-color="#1b86cc"/>
      </linearGradient>
    </defs>
    <polygon points="420,40 448,6 700,6 700,40" fill="#33a6d7"/>
    <polygon points="0,110 420,40 700,40 700,140 0,140" fill="url(#bandFill)"/>
  </svg>
  <div class="licences">AU61420 | BLD472913</div>
</section>

<section class="card card--back" aria-label="Business card back">
  <p class="back__name">Harbourline Refrigeration</p>
  <div class="back__web">
    <span class="back__rule"></span>
    <span>www.harbourlinerefrigeration.example</span>
    <span class="back__rule"></span>
  </div>
</section>

</body>
</html>
```